Exhibition stand - artwork only

we are attending a conference and have a 2-sided exhibition stand 3m x 2m. the expo organisers require the artwork immediately for the stand, hence the quick turnaround. Artwork is required for the front elevation and side elevation.

requirements:
JPG, TIFF or PDF
Front elevation Image is landscape, 100cm tall x 300cm wide
Brand colours attached
front elevation mock up attached
Design must work around the TV (see elevation pic)
Logo not required on front elevation.

side elevation graphics are split in two:
50cm wide x 200cm tall
135cm wide x 190cm tall
side elevation mock up attached
side elevation design should include a large logo.

Messaging (front elevation):
"Ask us about our Pretty Big Sector Announcement"

Info:
PBSA are the 1st letters of Pretty Big Sector Announcement. We work in the PBSA sector (which actually stands for Purpose built student accommodation). The first letters should be highlighted, or bigger, or bold - they must stand out and it must be obvious they read 'PBSA'.

Attached is some inspiration with the slide background we use, and an image background.

Design only, no print required.

```html
<!DOCTYPE html>
<html lang="en">
<head>
<meta charset="utf-8">
<title>Pretty Big Sector Announcement – Front Elevation</title>
<link rel="stylesheet" href="https://fonts.googleapis.com/css2?family=Raleway:wght@300;400;800&display=swap">
<style>
  :root {
    --blue-light: #3b82c8;
    --blue-mid: #3f6fbf;
    --blue-deep: #2c4f9e;
    --blue-dark: #1f3d86;
    --white: #ffffff;
    --frame-grey: #4a4a4a;
    --frame-black: #050505;
  }
  html, body {
    margin: 0;
    padding: 0;
    width: 1200px;
    height: 400px;
    overflow: hidden;
    background: var(--blue-mid);
  }
  .elevation {
    position: relative;
    width: 1200px;
    height: 400px;
    overflow: hidden;
    font-family: "Raleway", sans-serif;
    color: var(--white);
  }
  .backdrop {
    position: absolute;
    inset: 0;
    background:
      radial-gradient(ellipse 420px 380px at 600px 180px, rgba(120,160,220,0.35), transparent 70%),
      linear-gradient(100deg, var(--blue-light) 0%, var(--blue-mid) 40%, var(--blue-deep) 75%, var(--blue-dark) 100%);
  }
  .divider {
    position: absolute;
    left: 81px;
    top: 50px;
    width: 1.5px;
    height: 298px;
    background: var(--white);
  }
  .headline-line {
    position: absolute;
    left: 98px;
    margin: 0;
    line-height: 1;
    white-space: nowrap;
    font-weight: 300;
  }
  .intro { font-size: 36px; font-weight: 400; }
  .acronym-word { font-size: 67px; letter-spacing: 0.5px; }
  .initial { font-weight: 800; }
  .line-1 { top: 47px; }
  .line-2 { top: 83px; }
  .line-3 { top: 124px; }
  .line-4 { top: 182px; }
  .line-5 { top: 238px; }
  .line-6 { top: 291px; }
  .tv-zone {
    position: absolute;
    left: 704px;
    top: 28px;
    width: 445px;
    height: 254px;
    box-shadow: 4px 10px 14px rgba(0,0,0,0.35);
  }
</style>
</head>
<body>
<main class="elevation">
  <div class="backdrop" role="img" aria-label="Blue-toned photograph looking up at tall glass office towers against the sky"></div>

  <span class="divider"></span>

  <h1 class="headline">
    <span class="headline-line intro line-1">ASK US</span>
    <span class="headline-line intro line-2">ABOUT OUR</span>
    <span class="headline-line acronym-word line-3"><span class="initial">P</span>RETTY</span>
    <span class="headline-line acronym-word line-4"><span class="initial">B</span>IG</span>
    <span class="headline-line acronym-word line-5"><span class="initial">S</span>ECTOR</span>
    <span class="headline-line acronym-word line-6"><span class="initial">A</span>NNOUNCEMENT</span>
  </h1>

  <svg class="tv-zone" viewBox="0 0 445 254" aria-label="Position of the stand's TV">
    <rect x="0" y="0" width="445" height="254" fill="var(--frame-grey)"/>
    <polygon points="250,0 445,0 445,254 125,254" fill="var(--frame-black)"/>
    <rect x="7" y="6" width="432" height="242" fill="var(--white)"/>
  </svg>
</main>
</body>
</html>
```